Health Coach needs a Business Card Design

Need a really modern feminine business card design for a health and lifestyle coach. Needs to use geometric shapes, muted grey/blue/green pastels and black and white - see mood board attached and logo. The client likes black and white, modern, san serif with the use of lines and possibly a shadow leaf as in the mood board. Possibly put the tag line on the back or an icon of the logo. Logo is also attached. An icon of the logo would be great too.

Target Market(s)

Women (some men) aged 30 to 50.

Industry/Entity Type

Business

Contact Information for Business Card

Maren Tolvey
e-mail: hello@marentwell.net
website: marentwell.net
Phone: +610497268153

The tag line is "A balanced body for Life"

Font styles to use
Sans Serif

Colors
ecf7fb
cfeae6
000000
ffffff
f5f5f5

Requirements
Must have
• Black and white, logo, tag line and details
Nice to have
• Would be nice to incorporate the shadow palm.fern leaves as in the mood board and or geometric lines/shapes - see mood board. Could be either standard rectangle or would be happy with square too.
Should not have
• Flowers or decorations

```html
<!DOCTYPE html>
<html lang="en">
<head>
<meta charset="utf-8">
<title>Maren Tolvey — Business Card</title>
<link href="https://fonts.googleapis.com/css2?family=Open+Sans:wght@300;400;600&display=swap" rel="stylesheet">
<style>
  :root {
    --page-bg: #ecebe8;
    --card-bg: #ffffff;
    --ink: #555555;
    --ink-strong: #3f3f3f;
    --leaf-deep: #7e9ea3;
    --leaf-soft: #cfeae6;
    --leaf-mist: #ecf7fb;
  }
  * { margin: 0; padding: 0; box-sizing: border-box; }
  html, body {
    width: 1200px;
    height: 1000px;
    overflow: hidden;
    background: var(--page-bg);
    font-family: "Open Sans", sans-serif;
    color: var(--ink);
  }
  .card {
    position: absolute;
    top: 252px;
    width: 496px;
    height: 496px;
    background: var(--card-bg);
    box-shadow: 0 3px 10px rgba(0,0,0,0.18);
    overflow: hidden;
  }
  .card--front { left: 73px; }
  .card--back { left: 627px; }

  .brand-name {
    position: absolute;
    left: 0;
    width: 100%;
    text-align: center;
    font-family: "Open Sans", sans-serif;
    font-weight: 300;
    font-size: 34px;
    letter-spacing: 3px;
    color: var(--ink);
  }
  .card--front .brand-name { top: 84px; }
  .card--back .brand-name { top: 120px; }

  .tagline {
    position: absolute;
    top: 146px;
    left: 0;
    width: 100%;
    text-align: center;
    font-size: 12.5px;
    font-weight: 400;
    letter-spacing: 3.2px;
    text-transform: uppercase;
    color: var(--ink);
  }

  .contact {
    position: absolute;
    top: 276px;
    left: 0;
    width: 100%;
    text-align: center;
    font-size: 17px;
    line-height: 26px;
    color: var(--ink);
  }
  .contact-icons {
    display: flex;
    justify-content: center;
    gap: 8px;
    height: 16px;
    margin-bottom: 8px;
  }
  .contact-divider {
    width: 42px;
    height: 1px;
    background: var(--ink);
    margin: 16px auto 14px;
  }
  .contact-web strong { font-weight: 400; color: var(--ink-strong); }

  .leaf-shade {
    position: absolute;
  }
  .leaf-shade--lower { left: 0; top: 268px; width: 260px; height: 228px; }
  .leaf-shade--upper { left: 348px; top: 192px; width: 148px; height: 250px; }
</style>
</head>
<body>

  <section class="card card--front">
    <h1 class="brand-name">Maren Tolvey</h1>
    <p class="tagline">A balanced body for life</p>

    <div class="contact">
      <div class="contact-icons">
        <svg width="14" height="12" viewBox="0 0 14 12" aria-label="phone" role="img">
          <path d="M1 4 Q7 -1 13 4 L11 5 L10 3 Q7 2 4 3 L3 5 Z" fill="#555"/>
          <rect x="3" y="5" width="8" height="6" rx="1" fill="#555"/>
        </svg>
        <svg width="14" height="12" viewBox="0 0 14 12" aria-label="email" role="img">
          <rect x="1" y="2" width="12" height="9" fill="#555"/>
          <path d="M1 2 L7 7 L13 2" fill="none" stroke="#fff" stroke-width="1"/>
        </svg>
      </div>
      <p class="contact-phone">+610497268153</p>
      <p class="contact-email">hello@marentwell.net</p>
      <div class="contact-divider"></div>
      <p class="contact-web">www.<strong>marentwell</strong>.net</p>
    </div>
  </section>

  <section class="card card--back">
    <h2 class="brand-name">Maren Tolvey</h2>

    <svg class="leaf-shade leaf-shade--lower" viewBox="0 0 260 228" role="img" aria-label="watercolour palm fronds in muted blue-green">
      <defs>
        <linearGradient id="leafLower" x1="0" y1="1" x2="1" y2="0">
          <stop offset="0" stop-color="var(--leaf-deep)" stop-opacity="0.75"/>
          <stop offset="0.6" stop-color="var(--leaf-soft)" stop-opacity="0.7"/>
          <stop offset="1" stop-color="var(--leaf-mist)" stop-opacity="0.3"/>
        </linearGradient>
      </defs>
      <path d="M0 20 Q60 40 110 100 Q170 10 255 0 Q230 120 150 228 L0 228 Z" fill="url(#leafLower)"/>
    </svg>

    <svg class="leaf-shade leaf-shade--upper" viewBox="0 0 148 250" role="img" aria-label="watercolour palm frond in muted blue-green">
      <defs>
        <linearGradient id="leafUpper" x1="1" y1="0" x2="0" y2="1">
          <stop offset="0" stop-color="var(--leaf-deep)" stop-opacity="0.7"/>
          <stop offset="0.7" stop-color="var(--leaf-soft)" stop-opacity="0.6"/>
          <stop offset="1" stop-color="var(--leaf-mist)" stop-opacity="0.2"/>
        </linearGradient>
      </defs>
      <path d="M148 0 L148 250 Q110 200 100 150 Q40 110 0 45 Q60 20 148 0 Z" fill="url(#leafUpper)"/>
    </svg>
  </section>

</body>
</html>
```